Tobin's Butter dairy product for export market

We are starting a new brand for our butter range. We are looking for a premimum branding with family values. The product should be elligent and simle and easy for consumers to choose and easy for chefs,

A samples of our current brand and packing details in on the pack
target markets , China, Hong Kong, Asia, middle east
products will be sold in different size starting from small portion eg 7g to 1kg food service pack
product will be sold in 2 varients salted and unsalted

Target Market(s)

Australian Market and export market

Industry/Entity Type

Product

Colors
9bcb3c
fbed22

Requirements
Must have
• Pure butter
• packed in Australia
• nice fresh modern simple design
Nice to have
• Colours gold , green or any other suggestions welcome.
Should not have
• Any third party pictures of butter etc..

```html
<!DOCTYPE html>
<html lang="en">
<head>
<meta charset="utf-8">
<title>Tobin's Butter – 1kg carton dieline</title>
<link href="https://fonts.googleapis.com/css2?family=Cinzel:wght@500;700&family=Questrial&family=Roboto+Condensed:wght@400;700&display=swap" rel="stylesheet">
<style>
  :root{
    --board:#2f2f2f;
    --cream:#fdf9e4;
    --gold:#d89c44;
    --taupe:#a59a80;
    --title:#a99f84;
    --olive:#a7a45e;
    --magenta:#ec008c;
    --die:#0f5a60;
    --guide:#23b5e8;
    --ink:#1e1e1e;
  }
  html,body{margin:0;padding:0;overflow:hidden;background:var(--board);}
  .carton{position:relative;width:954px;height:1200px;background:var(--board);overflow:hidden;font-family:"Questrial",sans-serif;}
  .panel{position:absolute;background:var(--cream);}
  .dieline{position:absolute;left:0;top:0;pointer-events:none;}

  /* back panel, printed upside down */
  .back{left:161px;top:163px;width:632px;height:294px;}
  .back-inner{position:absolute;inset:0;transform:rotate(180deg);}
  .back-guide{position:absolute;left:19px;top:19px;right:19px;bottom:19px;border:1px dashed var(--guide);}
  .code-area{position:absolute;left:19px;top:19px;width:176px;height:256px;background:var(--magenta);}
  .back-title{position:absolute;left:203px;top:36px;width:180px;text-align:center;font-family:"Cinzel",serif;font-weight:700;font-size:17px;color:var(--title);letter-spacing:2px;white-space:nowrap;}
  .ingredients{position:absolute;left:224px;top:138px;width:150px;text-align:center;font-family:"Roboto Condensed",sans-serif;font-size:10px;line-height:11.5px;color:var(--ink);}
  .ingredients .gap{height:6px;}
  .nutrition{position:absolute;left:405px;top:33px;width:195px;border-collapse:collapse;font-family:"Roboto Condensed",sans-serif;font-size:8.5px;color:var(--ink);}
  .nutrition td{border:0.8px solid var(--ink);height:15.3px;padding:0 4px;white-space:nowrap;}
  .nutrition .head{font-weight:700;}

  /* front faces */
  .face{left:161px;width:793px;}
  .face-1{top:457px;height:286px;}
  .face-2{top:743px;height:294px;}
  .safe{position:absolute;left:20px;top:18px;width:595px;border:1px dashed var(--guide);}
  .face-1 .safe{height:250px;}
  .face-2 .safe{height:258px;}
  .stamp{position:absolute;left:75px;width:128px;height:128px;border-radius:50%;border:2px solid #ece1c2;background:radial-gradient(circle,#ead2a6 0 30%,transparent 31%);}
  .face-1 .stamp{top:31px;}
  .face-2 .stamp{top:42px;}
  .brand{position:absolute;left:107px;width:420px;text-align:center;font-family:"Cinzel",serif;font-weight:700;font-size:39px;color:var(--title);letter-spacing:2.5px;white-space:nowrap;}
  .face-1 .brand{top:100px;}
  .face-2 .brand{top:96px;}
  .variant{position:absolute;left:195px;font-size:13px;letter-spacing:9.2px;color:var(--gold);white-space:nowrap;}
  .face-1 .variant{top:155px;}
  .face-2 .variant{top:150px;}
  .band{position:absolute;left:0;right:0;background:var(--gold);border-top:10px solid var(--taupe);}
  .face-1 .band{top:183px;bottom:0;}
  .face-2 .band{top:190px;bottom:0;}
  .claim{position:absolute;left:205px;top:24px;font-size:24px;letter-spacing:5px;color:#fff;white-space:nowrap;}
  .net{position:absolute;left:30px;top:49px;font-family:"Cinzel",serif;font-weight:700;font-size:15px;color:#3a3a3a;white-space:nowrap;}
  .free-from{position:absolute;left:470px;top:42px;width:143px;text-align:right;font-size:10px;letter-spacing:1.4px;line-height:13px;color:#fff;white-space:nowrap;}
  .badges{position:absolute;left:570px;width:62px;}
  .face-1 .badges{top:17px;}
  .face-2 .badges{top:13px;}
  .badge{height:30px;margin-bottom:2px;border-radius:15px 0 0 15px;}
  .badge-a{background:var(--gold);}
  .badge-b{background:var(--olive);}

  /* top flap */
  .weight{position:absolute;left:288px;top:128px;font-family:"Questrial",sans-serif;font-size:14px;color:var(--gold);transform:rotate(180deg);}

  /* bottom flap imprint */
  .imprint{position:absolute;left:280px;top:1053px;width:392px;text-align:center;font-size:8px;line-height:10.4px;color:#4a4a4a;text-transform:uppercase;}
  .imprint p{margin:0 0 7px;}
</style>
</head>
<body>
<div class="carton">

  <svg class="dieline" width="954" height="1200" viewBox="0 0 954 1200">
    <g fill="none" stroke="var(--die)" stroke-width="0.8">
      <line x1="0" y1="163" x2="954" y2="163"/>
      <line x1="0" y1="457" x2="954" y2="457"/>
      <line x1="0" y1="743" x2="954" y2="743"/>
      <line x1="0" y1="1037" x2="954" y2="1037"/>
      <line x1="161" y1="0" x2="161" y2="1200"/>
      <line x1="793" y1="0" x2="793" y2="1200"/>
      <line x1="161" y1="163" x2="310" y2="0"/>
      <line x1="793" y1="163" x2="648" y2="0"/>
      <line x1="161" y1="1037" x2="300" y2="1200"/>
      <line x1="793" y1="1037" x2="660" y2="1200"/>
      <line x1="0" y1="310" x2="161" y2="457"/>
      <line x1="0" y1="890" x2="161" y2="743"/>
      <polyline points="125,495 52,600 125,705"/>
      <line x1="125" y1="495" x2="125" y2="705"/>
      <polyline points="793,1037 954,870"/>
    </g>
    <g fill="none" stroke="var(--die)" stroke-width="0.8" stroke-dasharray="5 4">
      <polyline points="205,145 325,20 630,20 750,145 205,145"/>
    </g>
    <g fill="none" stroke="var(--guide)" stroke-width="0.8" stroke-dasharray="5 4">
      <polyline points="205,1055 285,1140 675,1140 750,1055 205,1055"/>
    </g>
    <g fill="none" stroke="var(--guide)" stroke-width="0.8">
      <line x1="808" y1="0" x2="808" y2="1200"/>
      <line x1="793" y1="743" x2="954" y2="890"/>
      <polyline points="831,494 903,600 831,706"/>
    </g>
    <g stroke="var(--gold)" stroke-width="1.2">
      <line x1="284" y1="126" x2="284" y2="143"/>
      <line x1="413" y1="126" x2="413" y2="143"/>
      <line x1="541" y1="126" x2="541" y2="143"/>
      <line x1="669" y1="126" x2="669" y2="143"/>
    </g>
  </svg>

  <div class="weight">200g</div>

  <section class="panel back">
    <div class="back-inner">
      <div class="back-guide"></div>
      <div class="code-area"></div>
      <div class="back-title">Tobin's Butter</div>
      <div class="ingredients">
        <div>INGREDIENTS:</div>
        <div>CREAM (FROM <b>MILK</b>),</div>
        <div>WATER, LACTIC ACID,</div>
        <div>STARTER DISTILLATE</div>
        <div class="gap"></div>
        <div><b>MILK FAT:</b> 80% MIN</div>
        <div class="gap"></div>
        <div>PRODUCT OF AUSTRALIA</div>
        <div>STORE BELOW 4°C</div>
      </div>
      <table class="nutrition">
        <tr><td colspan="3" class="head">NUTRITION INFORMATION</td></tr>
        <tr><td colspan="3">SERVINGS PER PACK: 100</td></tr>
        <tr><td colspan="3">SERVING SIZE: 10g</td></tr>
        <tr><td></td><td colspan="2" class="head">Average Quantity</td></tr>
        <tr><td></td><td class="head">Per serving</td><td class="head">Per 100g</td></tr>
        <tr><td>Energy</td><td>302kJ</td><td>3020kJ</td></tr>
        <tr><td>Protein</td><td>Less than 1g</td><td>Less than 1g</td></tr>
        <tr><td>Fat (Total)</td><td>8.1g</td><td>81g</td></tr>
        <tr><td>– Saturated</td><td>5.48g</td><td>54.8g</td></tr>
        <tr><td>– Trans fat</td><td>Less than 1g</td><td>4.0g</td></tr>
        <tr><td colspan="3">Carbohydrates:</td></tr>
        <tr><td>– Total</td><td>Less than 1g</td><td>Less than 1g</td></tr>
        <tr><td>– Sugars</td><td>Less than 1g</td><td>Less than 1g</td></tr>
        <tr><td>Sodium</td><td>Less than 1mg</td><td>9mg</td></tr>
      </table>
    </div>
  </section>

  <section class="panel face face-1">
    <div class="stamp" role="img" aria-label="Faint Australian packed and made seal with map of Australia"></div>
    <div class="brand">Tobin's Butter</div>
    <div class="variant">LACTIC UNSALTED</div>
    <div class="badges">
      <div class="badge badge-a" role="img" aria-label="Halal certification badge"></div>
      <div class="badge badge-b" role="img" aria-label="Vegetarian friendly badge"></div>
    </div>
    <div class="band">
      <div class="claim">PURE BUTTER</div>
      <div class="net">1 kg NET</div>
      <div class="free-from">NO PRESERVATIVES<br>NO VEGETABLE FATS</div>
    </div>
    <div class="safe"></div>
  </section>

  <section class="panel face face-2">
    <div class="stamp" role="img" aria-label="Faint Australian packed and made seal with map of Australia"></div>
    <div class="brand">Tobin's Butter</div>
    <div class="variant">LACTIC UNSALTED</div>
    <div class="badges">
      <div class="badge badge-a" role="img" aria-label="Halal certification badge"></div>
      <div class="badge badge-b" role="img" aria-label="Vegetarian friendly badge"></div>
    </div>
    <div class="band">
      <div class="claim">PURE BUTTER</div>
      <div class="net">1 kg NET</div>
      <div class="free-from">NO PRESERVATIVES<br>NO VEGETABLE FATS</div>
    </div>
    <div class="safe"></div>
  </section>

  <div class="imprint">
    <p>Packed by :<br>Southern Creamery Works Pty Ltd<br>Phone: +61 3 9000 1234 Email: info@southerncreamery.example<br>12 Harbour Lane Riverside Victoria 3000 Australia<br>Reg No: 5817</p>
    <p>Produced &amp; packed for :<br>Larkfield Trading Pty Ltd<br>4 Wattle Court Greenvale Victoria 3059 Australia</p>
  </div>

</div>
</body>
</html>
```